Redesign of an insurance website

Attached is an insurance website that I need to redesign. Currently the website is too dark. I like for example www.brenvalo.com . Could you make the website lighter and change the structure a little so that it is more user friendly?

Industry/Entity Type

Insurance

Number of Pages Required

4 page

```html
<!DOCTYPE html>
<html lang="cs">
<head>
<meta charset="utf-8">
<title>Krytopis.cz – Pojištění</title>
<link href="https://fonts.googleapis.com/css2?family=Lato:wght@400;700;900&family=Ubuntu:wght@400;500&display=swap" rel="stylesheet">
<style>
  :root{
    --blue:#2e8cf5;
    --blue-dark:#1f6fe0;
    --blue-footer:#2a84f0;
    --orange:#f77f1a;
    --text:#444;
    --muted:#777;
    --hero-bg:#eaf4fc;
    --grey-bg:#f2f2f2;
    --line:#d6d6d6;
    --white:#fff;
  }
  *{box-sizing:border-box;margin:0;padding:0}
  html,body{width:841px;height:1200px;overflow:hidden;background:var(--white)}
  body{position:relative;font-family:"Lato",sans-serif;color:var(--text)}
  .abs{position:absolute}

  /* Header */
  .site-header{left:0;top:0;width:841px;height:75px;background:var(--white);border-bottom:1px solid var(--line)}
  .nav-link{font-size:11px;color:#555;top:33px;letter-spacing:.1px}
  .brand{left:333px;top:26px;font-family:"Lato",sans-serif;font-weight:900;font-size:20px;color:var(--blue);letter-spacing:.5px}
  .social{top:28px;width:21px;height:21px;border:1.5px solid var(--blue);border-radius:50%}

  /* Hero */
  .hero{left:0;top:75px;width:841px;height:418px;background:linear-gradient(180deg,#e6f2fc 0%,#f3f8fd 70%,#ffffff 100%)}
  .hero-figure{left:84px;top:105px;width:152px;height:335px;border-radius:70px 70px 10px 10px;background:linear-gradient(180deg,#f3c9a4 0%,#c8392b 38%,#3d4a55 75%,#e9eef2 100%);opacity:.85}
  .hero-title{left:256px;top:140px;width:260px;font-family:"Ubuntu",sans-serif;font-weight:500;font-size:21px;line-height:25px;color:var(--blue)}
  .benefits{left:257px;top:210px;list-style:none}
  .benefits li{display:flex;align-items:center;height:23.2px;font-size:11px;color:#555}
  .benefits svg{margin-right:7px;flex:none}

  .quote-card{left:531px;top:143px;width:237px;height:212px;background:var(--white);box-shadow:0 2px 10px rgba(46,140,245,.18)}
  .quote-badge{left:615px;top:104px;width:64px;height:64px;border-radius:50%;background:var(--blue);border:3px solid var(--white);box-shadow:0 0 0 1.5px var(--blue)}
  .quote-title{left:531px;top:176px;width:237px;text-align:center;font-family:"Ubuntu",sans-serif;font-size:12px;color:var(--blue)}
  .field{left:555px;width:188px;height:24px;border:1px solid #cfd6dc;font-size:9px;color:#999;padding:6px 10px}
  .agree{left:555px;top:290px;font-size:6.5px;color:#666;display:flex;align-items:center}
  .agree span{width:9px;height:9px;border:1px solid #bbb;margin-right:6px;display:inline-block}
  .btn-submit{left:555px;top:310px;width:188px;height:29px;background:var(--orange);color:var(--white);font-size:10.5px;text-align:center;line-height:29px}

  .cat{width:90px;text-align:center;font-family:"Ubuntu",sans-serif;font-size:9.5px;line-height:13px;color:#777;top:380px}
  .cat .ring{width:50px;height:50px;margin:0 auto 6px;border-radius:50%;border:1.5px solid var(--blue);display:flex;align-items:center;justify-content:center;background:var(--white)}
  .cat.active .ring{background:var(--blue)}
  .arrow{top:408px}

  /* Offer */
  .offer{left:0;top:493px;width:841px;height:264px;background:linear-gradient(180deg,#ececec 0%,#f7f7f7 100%);border-bottom:1px solid #e2e2e2}
  .offer-title{left:0;top:540px;width:841px;text-align:center;font-family:"Ubuntu",sans-serif;font-size:20px;line-height:26px;color:var(--orange)}
  .offer-text{left:140px;top:609px;width:561px;text-align:center;font-size:9.5px;line-height:17.5px;color:#555}
  .btn-solid{left:363px;top:679px;width:109px;height:28px;background:var(--orange);color:var(--white);font-size:10.5px;text-align:center;line-height:28px}

  /* How it works */
  .how-title{left:93px;top:813px;font-family:"Ubuntu",sans-serif;font-size:19px;color:#333}
  .how-text{left:93px;width:260px;font-size:10px;line-height:17.5px;color:#555}
  .btn-outline{left:93px;top:968px;width:108px;height:28px;border:1.5px solid var(--orange);color:var(--orange);font-size:10.5px;text-align:center;line-height:25px}
  .how-illustration{left:358px;top:815px;width:396px;height:180px;border-radius:6px;background:linear-gradient(135deg,#eef5fe 0%,#dcebfd 100%)}

  /* Newsletter & footer */
  .newsletter{left:0;top:1060px;width:841px;height:88px;background:var(--blue)}
  .news-title{left:107px;top:1092px;font-size:20px;color:var(--white)}
  .news-input{left:296px;top:1087px;width:437px;height:37px;border:1px solid rgba(255,255,255,.8);border-radius:19px;color:var(--white);font-size:12px;padding:10px 23px}
  .btn-subscribe{left:626px;top:1091px;width:103px;height:29px;border-radius:15px;background:var(--orange);color:var(--white);font-size:12.5px;font-weight:700;text-align:center;line-height:29px}
  .site-footer{left:0;top:1148px;width:841px;height:52px;background:var(--blue-footer);color:#e6f0ff;font-size:10px;text-align:center;line-height:46px}
</style>
</head>
<body>

<header class="abs site-header"></header>
<a class="abs nav-link" style="left:84px">ONAS</a>
<a class="abs nav-link" style="left:139px">CASTE DOTAZY</a>
<a class="abs nav-link" style="left:241px">KONTAKT</a>
<div class="abs brand">KRYTOPIS.CZ</div>
<a class="abs nav-link" style="left:529px">PRIHALASIT SE</a>
<a class="abs nav-link" style="left:617px">REGISTROVAT</a>
<span class="abs social" style="left:697px"></span>
<span class="abs social" style="left:721px"></span>
<span class="abs social" style="left:745px"></span>

<section class="abs hero"></section>
<div class="abs hero-figure" role="img" aria-label="Ilustrace poradce v červeném svetru ukazujícího na nabídku"></div>

<h1 class="abs hero-title">Proc hledat Pojisteni pres Krytopis.cz?</h1>
<ul class="abs benefits">
  <li><svg width="13" height="13" viewBox="0 0 13 13"><circle cx="6.5" cy="6.5" r="6.5" fill="#f77f1a"/><path d="M3.5 6.6l2 2 4-4.2" stroke="#fff" stroke-width="1.6" fill="none"/></svg>Arcu Morbi porta libero id ullamcorper</li>
  <li><svg width="13" height="13" viewBox="0 0 13 13"><circle cx="6.5" cy="6.5" r="6.5" fill="#f77f1a"/><path d="M3.5 6.6l2 2 4-4.2" stroke="#fff" stroke-width="1.6" fill="none"/></svg>nonummy nibh ligula pulvinar</li>
  <li><svg width="13" height="13" viewBox="0 0 13 13"><circle cx="6.5" cy="6.5" r="6.5" fill="#f77f1a"/><path d="M3.5 6.6l2 2 4-4.2" stroke="#fff" stroke-width="1.6" fill="none"/></svg>Aetus eget consectetuer augue nisi</li>
  <li><svg width="13" height="13" viewBox="0 0 13 13"><circle cx="6.5" cy="6.5" r="6.5" fill="#f77f1a"/><path d="M3.5 6.6l2 2 4-4.2" stroke="#fff" stroke-width="1.6" fill="none"/></svg>Puis lacus Ut ac mi quis lacus mollis aliquam</li>
  <li><svg width="13" height="13" viewBox="0 0 13 13"><circle cx="6.5" cy="6.5" r="6.5" fill="#f77f1a"/><path d="M3.5 6.6l2 2 4-4.2" stroke="#fff" stroke-width="1.6" fill="none"/></svg>Curabitur iaculis tempus eros</li>
  <li><svg width="13" height="13" viewBox="0 0 13 13"><circle cx="6.5" cy="6.5" r="6.5" fill="#f77f1a"/><path d="M3.5 6.6l2 2 4-4.2" stroke="#fff" stroke-width="1.6" fill="none"/></svg>Curabitur vel mi sit amet magna</li>
</ul>

<div class="abs quote-card"></div>
<div class="abs quote-badge">
  <svg width="58" height="58" viewBox="0 0 58 58"><path d="M16 30h26l-3 6H19z M20 30l4-6h10l4 6" stroke="#fff" stroke-width="2" fill="none"/><circle cx="22" cy="37" r="2" fill="#fff"/><circle cx="36" cy="37" r="2" fill="#fff"/></svg>
</div>
<div class="abs quote-title">Havarijnf Pojistenf</div>
<div class="abs field" style="top:204px">Your Name</div>
<div class="abs field" style="top:232px">Phone</div>
<div class="abs field" style="top:259px">Email</div>
<div class="abs agree"><span></span>Souhlasim s podminkami pouziti</div>
<div class="abs btn-submit">SUBMIT NOW</div>

<svg class="abs arrow" style="left:262px" width="12" height="20" viewBox="0 0 12 20"><path d="M10 2L3 10l7 8" stroke="#999" stroke-width="2" fill="none"/></svg>
<div class="abs cat active" style="left:278px"><div class="ring"><svg width="30" height="20" viewBox="0 0 30 20"><path d="M3 10h24l-3 6H6z M7 10l4-6h8l4 6" stroke="#fff" stroke-width="1.8" fill="none"/></svg></div>Havarijnf<br>Pojistenf</div>
<div class="abs cat" style="left:368px"><div class="ring"><svg width="28" height="28" viewBox="0 0 28 28"><path d="M4 16l20-9-3 4-8 4 3 8-3 1-4-7-4 1z" stroke="#2e8cf5" stroke-width="1.6" fill="none" stroke-linejoin="round"/></svg></div>Cestovnf<br>Pojistenf</div>
<div class="abs cat" style="left:455px"><div class="ring"><svg width="28" height="28" viewBox="0 0 28 28"><path d="M4 14L14 5l10 9 M7 12v11h14V12 M12 23v-6h4v6" stroke="#2e8cf5" stroke-width="1.8" fill="none" stroke-linejoin="round"/></svg></div>Pojistenf<br>Domova</div>
<div class="abs cat" style="left:545px"><div class="ring"><svg width="30" height="22" viewBox="0 0 30 22"><path d="M3 12l3-7h18l3 7v6H3z" fill="#2e8cf5"/><rect x="8" y="7" width="14" height="4" fill="#fff"/><circle cx="8" cy="15" r="1.6" fill="#fff"/><circle cx="22" cy="15" r="1.6" fill="#fff"/></svg></div>Povinne<br>Rucenf</div>
<div class="abs cat" style="left:637px;top:379px"><div class="ring"><svg width="32" height="24" viewBox="0 0 32 24"><path d="M3 14h26l-4 6H8z M9 14l3-5h8l3 5" stroke="#2e8cf5" stroke-width="1.7" fill="none" stroke-linejoin="round"/></svg></div>Boat<br>Insurance</div>
<svg class="abs arrow" style="left:730px" width="12" height="20" viewBox="0 0 12 20"><path d="M2 2l7 8-7 8" stroke="#999" stroke-width="2" fill="none"/></svg>

<section class="abs offer"></section>
<h2 class="abs offer-title">Uzavreli jste v minulosti nevyhodnou<br>pojistku? Zbavte se ji!</h2>
<p class="abs offer-text">Vivamus porttitor purus nisi eleifend libero a tempus libero lectus feugiat felis Morbi diam mauris viverra in gravida eu mattis in ante Morbi eget arcu Morbi porta libero id ullamcorper nonummy nibh ligula pulvinar metus eget consectetuer augue nisi quis lacus Ut ac mi quis lacus mollis aliquam Curabitur iaculis tempus eros Curabitur</p>
<a class="abs btn-solid">READ MORE</a>

<h2 class="abs how-title">Jak to Funguje</h2>
<p class="abs how-text" style="top:849px">Vivamus porttitor purus nisi eleifend libero a tempus libero lectus feugiat felis Morbi diam mau</p>
<p class="abs how-text" style="top:893px">mattis in ante Morbi eget arcu Morbi porta libero id ullamcorper nonummy nibh ligula pulvinar metus eget consectetuer augue nisi quis lacus Ut</p>
<a class="abs btn-outline">READ MORE</a>
<div class="abs how-illustration" role="img" aria-label="Liniová ilustrace týmu u počítačů obklopeného ikonami dokumentů, grafů a komunikace"></div>

<section class="abs newsletter"></section>
<div class="abs news-title">Newsletter Sign Up</div>
<div class="abs news-input">Email address</div>
<a class="abs btn-subscribe">Subscribe</a>

<footer class="abs site-footer">© 2017 Company Name &nbsp;All right reserved &nbsp;Terms of Use</footer>

</body>
</html>
```